Lumo Tails

im a dog walker, pet sitter and dog groomer. I can look after all pets from once a day pop in feeds of cats to small holdings and exotics. have 10 years experience in the industry. I can look after peoples dogs for the day while they are out or for longer if on holiday. I walk dogs when people are at work so the dogs get to have fun too. I do house sitting so all your animals are looked after together. you have designed my business cards and I wanted the 'lumo tails' with the paw to be the same on the leaflets. I have spoken to brandlark and they have sent a pdf file of business card and said it can be cropped. please let me know if this cant be done
im also a qualified canine hydrotherapist

Target Market(s)

pet owners

Industry/Entity Type

Pet

Requirements
Must have
• my phone number 07835204617
• email lumotails@mailnest.co.uk
• area; Tunbridge wells, Sevenoaks and surrounding areas
• I want it almost done as bullet points with the main things being the dog walking and the pet sitting.
Nice to have
• cartoon animals like business card not the cartoons with big eyes

```html
<!DOCTYPE html>
<html lang="en">
<head>
<meta charset="utf-8">
<title>Lumo Tails – Leaflet</title>
<link rel="stylesheet" href="https://fonts.googleapis.com/css2?family=Berkshire+Swash&family=Open+Sans:wght@400;600;700&display=swap">
<style>
  :root {
    --purple: #7b5ea7;
    --yellow: #f4c95d;
    --green: #8fbf5a;
    --sky: #2a9fd8;
    --sky-light: #8fd3f0;
    --paper: #f3f2ef;
    --paper-shade: #e4e2de;
    --ink: #2f2f33;
    --white: #ffffff;
    --grass-light: #86c24a;
    --grass-dark: #3f7a24;
    --fur-cream: #eadcc4;
    --fur-tan: #c9a070;
    --shirt-pink: #e98fae;
  }
  * { box-sizing: border-box; margin: 0; padding: 0; }
  html, body { width: 973px; height: 1200px; overflow: hidden; background: #ececec; }
  .leaflet {
    position: relative; width: 973px; height: 1200px; overflow: hidden;
    background: var(--paper);
    font-family: "Open Sans", sans-serif; color: var(--ink);
  }
  .garden-photo {
    position: absolute; left: 0; top: 0; width: 973px; height: 470px;
    background: linear-gradient(180deg, #2f5d22 0%, var(--grass-dark) 8%, var(--grass-light) 40%, #9ccd52 100%);
  }
  .pets-photo {
    position: absolute; left: 30px; top: 215px; width: 940px; height: 230px;
    background: radial-gradient(ellipse at 50% 65%, rgba(234,220,196,0.85) 0%, rgba(201,160,112,0.55) 45%, rgba(201,160,112,0) 72%);
  }
  .shapes { position: absolute; inset: 0; }
  .paper-texture {
    position: absolute; left: 0; top: 380px; width: 973px; height: 680px;
    background: radial-gradient(ellipse at 35% 45%, var(--paper) 0%, var(--paper-shade) 100%);
  }
  .owner-photo {
    position: absolute; left: 600px; top: 395px; width: 373px; height: 640px;
    border-radius: 46% 0 0 40% / 30% 0 0 30%;
    background:
      radial-gradient(ellipse at 40% 42%, var(--fur-cream) 0%, rgba(234,220,196,0.9) 32%, rgba(234,220,196,0) 55%),
      linear-gradient(170deg, #c28a6a 0%, var(--shirt-pink) 45%, #d8789a 100%);
    opacity: 0.9;
  }
  .experience-badge {
    position: absolute; left: 60px; top: 98px; width: 220px; height: 220px; border-radius: 50%;
    background: var(--sky); border: 9px solid var(--yellow);
    display: flex; align-items: center; justify-content: center; text-align: center;
    font-family: "Berkshire Swash", serif; color: var(--white); font-size: 31px; line-height: 1.12;
  }
  .hydro-tag {
    position: absolute; left: 503px; top: 74px; width: 440px; height: 42px; border-radius: 21px;
    background: var(--yellow); display: flex; align-items: center; justify-content: center;
    font-weight: 600; font-size: 20px; color: var(--ink);
  }
  .brand {
    position: absolute; left: 92px; top: 500px; display: flex; align-items: center; gap: 24px;
  }
  .brand-dot { width: 100px; height: 100px; border-radius: 50%; background: var(--yellow); flex: none; }
  .brand-name { font-family: "Berkshire Swash", serif; font-size: 60px; line-height: 1.05; color: var(--purple); }
  .area {
    position: absolute; left: 50px; top: 668px; width: 450px; text-align: center;
    border-top: 1px solid #8a8a8a; padding-top: 12px; font-size: 23px; line-height: 1.4;
  }
  .services { position: absolute; left: 45px; top: 790px; width: 460px; list-style: none; text-align: center; }
  .services li {
    font-weight: 600; font-size: 27px; height: 46px; line-height: 43px;
    border-bottom: 2px solid var(--sky-light);
  }
  .contact { position: absolute; left: 0; right: 0; bottom: 0; height: 140px; color: var(--white); }
  .contact-name { position: absolute; left: 48px; top: 0; font-family: "Berkshire Swash", serif; font-size: 46px; }
  .contact-email { position: absolute; left: 48px; top: 74px; font-size: 30px; font-weight: 600; }
  .contact-phone { position: absolute; right: 42px; top: 64px; font-size: 44px; font-weight: 700; letter-spacing: 1px; }
</style>
</head>
<body>
<main class="leaflet">
  <div class="garden-photo" role="img" aria-label="Photo of a mown garden lawn"></div>
  <div class="pets-photo" role="img" aria-label="Photo of a kitten, French bulldog puppy, kittens, a retriever puppy and a budgie lined up along the lawn edge"></div>

  <svg class="shapes" width="973" height="1200" viewBox="0 0 973 1200" aria-hidden="true">
    <path d="M0 400 C140 350 300 335 470 350 L470 372 C300 362 140 390 0 440 Z" fill="var(--purple)"/>
    <path d="M0 440 C140 390 300 362 470 372 C660 385 820 375 973 360 L973 385 C820 400 650 405 470 398 C300 392 140 420 0 470 Z" fill="var(--yellow)"/>
  </svg>
  <svg class="shapes" width="973" height="1200" viewBox="0 0 973 1200" aria-hidden="true">
    <path d="M0 470 C140 420 300 392 470 398 C650 405 820 400 973 385 L973 1060 L0 1060 Z" fill="var(--paper)"/>
  </svg>

  <div class="owner-photo" role="img" aria-label="Photo of a smiling woman in a pink top hugging a pale Labrador puppy"></div>

  <svg class="shapes" width="973" height="1200" viewBox="0 0 973 1200" aria-hidden="true">
    <path d="M0 1020 C260 985 600 1045 973 975 L973 1000 C640 1060 280 1010 0 1045 Z" fill="var(--yellow)"/>
    <path d="M620 1035 C760 1030 880 1010 973 995 L973 1050 C860 1050 740 1050 620 1035 Z" fill="var(--green)"/>
    <path d="M0 1045 C280 1012 640 1062 973 1020 L973 1032 C640 1075 280 1030 0 1058 Z" fill="var(--sky-light)"/>
    <path d="M0 1058 C280 1030 640 1075 973 1032 L973 1200 L0 1200 Z" fill="var(--purple)"/>
  </svg>

  <div class="experience-badge">10 Years<br>Experience<br>in animal<br>industry</div>
  <div class="hydro-tag">Qualified Canine Hydrotherapist</div>

  <div class="brand">
    <span class="brand-dot"></span>
    <span class="brand-name">Lumo<br>Tails</span>
  </div>

  <p class="area">Tunbridge Wells, Sevenoaks<br>and Surrounding Areas</p>

  <ul class="services">
    <li>Dog walking</li>
    <li>Pet/House sitting</li>
    <li>Dog Grooming</li>
    <li>Small holder knowledge</li>
  </ul>

  <footer class="contact">
    <p class="contact-name">Kira Dale</p>
    <p class="contact-email">lumotails@mailnest.co.uk</p>
    <p class="contact-phone">07835.204.617</p>
  </footer>
</main>
</body>
</html>
```